Luxury Brand Real Estate For Sale sign

**Update** I've added some examples from the internet of other signs that have a look similar to what I would like to see. I do not want my personal name in the sign. And the word FOR SALE Does not need to be so large - it can be more subtle.
I want to create a Real Estate for sale sign for my company that will be used for luxury/higher end real estate listings. I’m sharing my business card as well as a logo with new teal color to show what we're moving towards: we’re using Teal, white, black and gold.
Hoping the sign is simple, sophisticated and eye catching.
The sign should be 24" wide by 30" tall including the company name: Harbor Crest Realty Group and our logo, office phone number 727-555-0148 and website www.hcrgexample.com the words "For Sale"
Optional to add this e-mail address info@hcrgexample.com to the sign
Target Market(s)
Luxury home buyers
Industry/Entity Type
Real Estate
Look and feel

```html
<!DOCTYPE html>
<html lang="en">
<head>
<meta charset="utf-8">
<title>Harbor Crest Realty Group – For Sale Signs</title>
<link rel="stylesheet" href="https://fonts.googleapis.com/css2?family=Prompt:wght@300;400;600&display=swap">
<style>
  :root {
    --backdrop: #d9dadc;
    --ink: #1c191d;
    --teal: #0f8280;
    --paper: #ffffff;
  }
  * { margin: 0; padding: 0; box-sizing: border-box; }
  html, body { width: 960px; height: 1200px; overflow: hidden; }
  body {
    position: relative;
    background: var(--backdrop);
    font-family: "Prompt", sans-serif;
  }
  .sign { position: absolute; width: 411px; height: 514px; }
  .sign--classic { left: 60px; top: 77px; background: var(--paper); }
  .sign--agent { left: 489px; top: 77px; background: var(--paper); }
  .sign--bold { left: 274px; top: 608px; background: var(--ink); }

  .panel { position: absolute; }
  .panel--dark { background: var(--ink); }
  .panel--teal { background: var(--teal); }

  .line { position: absolute; line-height: 1; white-space: nowrap; }
  .center { left: 0; right: 0; text-align: center; }
  .rule { position: absolute; height: 1px; background: var(--paper); }

  .brand-stack {
    position: absolute; left: 17px; top: 16px; width: 377px; height: 226px;
    display: flex; flex-direction: column; align-items: center; justify-content: center;
    color: var(--teal); font-weight: 400; font-size: 31px; letter-spacing: 2px;
    text-transform: uppercase; line-height: 1.2; text-align: center;
  }
  .brand-row {
    position: absolute; display: flex; align-items: center; gap: 12px;
    color: var(--teal); font-weight: 400; font-size: 18px; letter-spacing: 0.5px;
    text-transform: uppercase; white-space: nowrap;
  }
  .brand-row .mark { width: 26px; height: 26px; border: 2px solid var(--teal); }

  .for-sale { color: var(--teal); font-weight: 400; }
  .agent-name { color: var(--paper); font-weight: 400; }
  .agent-title { color: var(--paper); font-weight: 400; }
  .phone { color: var(--paper); font-weight: 300; }
  .web { font-weight: 600; letter-spacing: 0.5px; }
</style>
</head>
<body>

  <!-- Sign: logo panel, headline, contact band -->
  <section class="sign sign--classic">
    <div class="panel panel--dark" style="left:17px;top:16px;width:377px;height:226px;"></div>
    <div class="brand-stack"><span>Harbor Crest</span><span>Realty Group</span></div>
    <div class="line center for-sale" style="top:334px;font-size:54px;letter-spacing:3px;">FOR SALE</div>
    <div class="panel panel--teal" style="left:17px;top:332px;width:377px;height:148px;"></div>
    <div class="line center agent-name" style="top:344px;font-size:34px;letter-spacing:0.5px;">Morgan Ellery</div>
    <div class="line center agent-title" style="top:379px;font-size:17px;letter-spacing:0.5px;">Real Estate Broker</div>
    <div class="rule" style="left:124px;width:164px;top:412px;"></div>
    <div class="line center phone" style="top:425px;font-size:42px;">727-555-0148</div>
    <div class="line center web" style="top:486px;font-size:16px;color:var(--teal);font-weight:400;">www.hcrgexample.com</div>
  </section>

  <!-- Sign: logo strip, agent band, headline below -->
  <section class="sign sign--agent">
    <div class="panel panel--dark" style="left:17px;top:16px;width:377px;height:136px;"></div>
    <div class="brand-row" style="left:0;right:0;justify-content:center;top:71px;">
      <span class="mark"></span><span>Harbor Crest Realty Group</span>
    </div>
    <div class="panel panel--teal" style="left:17px;top:170px;width:377px;height:253px;"></div>
    <div class="line center agent-name" style="top:251px;font-size:38px;letter-spacing:1px;">Morgan Ellery</div>
    <div class="rule" style="left:60px;width:291px;top:294px;"></div>
    <div class="line center phone" style="top:297px;font-size:45px;">727-555-0148</div>
    <div class="line center web" style="top:393px;font-size:15px;color:var(--paper);">www.hcrgexample.com</div>
    <div class="line center for-sale" style="top:431px;font-size:67px;letter-spacing:3px;">FOR SALE</div>
  </section>

  <!-- Sign: dark, large headline -->
  <section class="sign sign--bold">
    <div class="brand-row" style="left:44px;top:50px;">
      <span class="mark"></span><span>Harbor Crest Realty Group</span>
    </div>
    <div class="line for-sale" style="left:38px;top:127px;font-size:116px;font-weight:300;">FOR</div>
    <div class="line for-sale" style="left:38px;top:222px;font-size:116px;font-weight:300;">SALE</div>
    <div class="line agent-name" style="left:44px;top:358px;font-size:27px;font-weight:600;letter-spacing:0.5px;">Morgan Ellery</div>
    <div class="line phone" style="left:42px;top:392px;font-size:47px;font-weight:600;">727-555-0148</div>
    <div class="rule" style="left:45px;width:68px;top:451px;height:2px;"></div>
    <div class="line web" style="left:45px;top:465px;font-size:16px;color:var(--teal);">www.hcrgexample.com</div>
  </section>

</body>
</html>
```